Calm Harbor Blueprint

I need a on page electronic flyer for this coaching program. I want a silhouette to accompany the case the copy starts with. I have the copy written but need it put together in a striking way.

Target Market(s)

towards higher net worth individuals

Industry/Entity Type

Electronic

```html
<!DOCTYPE html>
<html lang="en">
<head>
<meta charset="utf-8">
<title>Calm Harbor Blueprint – Coaching Program Flyer</title>
<link rel="stylesheet" href="https://fonts.googleapis.com/css2?family=Arimo:wght@400;700&family=Arvo:wght@700&family=Libre+Baskerville:wght@700&display=swap">
<style>
  :root {
    --navy: #2b1f78;
    --ink: #111111;
    --orange-head: #cf6a2a;
    --band-yellow: #f6bf0e;
    --band-orange: #e6771c;
    --curve-blue: #1d6fc0;
    --teal: #1d9a9c;
    --purple: #8d1f7c;
    --rust: #a9402b;
    --olive: #9a8e35;
    --paper: #ffffff;
  }
  * { margin: 0; padding: 0; box-sizing: border-box; }
  html, body { width: 1200px; height: 929px; overflow: hidden; background: var(--paper); }
  .flyer { position: relative; width: 1200px; height: 929px; font-family: "Arimo", Arial, sans-serif; color: var(--ink); }

  .headline {
    position: absolute; top: 30px; left: 0; width: 1200px; text-align: center;
    font-family: "Libre Baskerville", Georgia, serif; font-weight: 700;
    font-size: 35px; color: var(--navy); letter-spacing: 0.2px;
  }
  .top-rule { position: absolute; left: 32px; top: 87px; width: 1131px; height: 12px; background: var(--ink); }

  .hero-photo {
    position: absolute; left: 32px; top: 99px; width: 413px; height: 540px;
    background: linear-gradient(180deg, #8fb2cf 0%, #5d7f9b 35%, #22303c 62%, #07090b 100%);
  }

  .title { position: absolute; left: 483px; top: 126px; font-weight: 700; font-size: 29px; color: var(--orange-head); }
  .subtitle { position: absolute; left: 527px; top: 164px; font-weight: 700; font-size: 27px; color: var(--orange-head); }

  .story { position: absolute; left: 472px; top: 217px; width: 672px; font-size: 15.2px; line-height: 18.2px; }
  .story p { margin-bottom: 18px; }

  .bands { position: absolute; left: 0; top: 0; width: 1200px; height: 929px; }

  .program-label {
    position: absolute; left: 54px; top: 638px;
    font-family: "Arvo", Georgia, serif; font-weight: 700; font-size: 16px; color: var(--ink);
  }
  .benefits { position: absolute; left: 44px; top: 662px; width: 467px; list-style: none; }
  .benefits li {
    height: 25px; line-height: 23px; padding-left: 20px; position: relative;
    color: #fff; font-weight: 700; font-size: 12.5px; border: 1px solid #e9e4c8; margin-bottom: 0.5px;
  }
  .benefits li::before {
    content: ""; position: absolute; left: 8px; top: 8px; width: 5px; height: 5px;
    border-top: 2px solid #fff; border-right: 2px solid #fff; transform: rotate(45deg);
  }
  .benefits .teal { background: var(--teal); }
  .benefits .purple { background: var(--purple); }
  .benefits .rust { background: var(--rust); }
  .benefits .olive { background: var(--olive); }

  .offer { position: absolute; left: 46px; top: 782px; list-style: none; font-weight: 700; font-size: 15.5px; }
  .offer li { position: relative; padding-left: 16px; height: 27px; }
  .offer li::before {
    content: ""; position: absolute; left: 1px; top: 6px; width: 5px; height: 5px;
    border-top: 2px solid var(--ink); border-right: 2px solid var(--ink); transform: rotate(45deg);
  }

  .coach-name {
    position: absolute; left: 895px; top: 710px; transform: rotate(-18deg); transform-origin: left center;
    font-family: "Arvo", Georgia, serif; font-weight: 700; font-size: 27px; color: var(--ink); white-space: nowrap;
  }
  .coach-bio {
    position: absolute; right: 41px; top: 784px; width: 400px; text-align: right;
    font-size: 14.2px; line-height: 17px; color: var(--ink);
  }
</style>
</head>
<body>
<main class="flyer">
  <h1 class="headline">Sometimes the best financial advice isn't about numbers...</h1>
  <div class="top-rule"></div>

  <div class="hero-photo" role="img" aria-label="Silhouette of a worried man seated on a chair, head in hand, by a window overlooking the sea"></div>

  <svg class="bands" viewBox="0 0 1200 929" aria-hidden="true">
    <path d="M32,604 Q420,592 850,796 Q480,852 32,858 Z" fill="var(--band-yellow)"/>
    <path d="M32,604 Q420,592 850,796" fill="none" stroke="var(--curve-blue)" stroke-width="5"/>
    <path d="M32,858 Q480,852 850,796 Q1010,768 1163,698 L1163,883 L32,883 Z" fill="var(--band-orange)"/>
    <path d="M32,858 Q480,852 850,796 Q1010,768 1163,698" fill="none" stroke="var(--ink)" stroke-width="4"/>
  </svg>

  <h2 class="title">Calm Harbor Blueprint</h2>
  <h3 class="subtitle">From Financial Worries to Wealth Satisfaction</h3>

  <section class="story">
    <p>A 49 year old attorney, Steve was used to success and rising net worth. But with huge losses in the market crash, layoffs at his firm, his kids heading for college and the stagnant economy stretching ahead, his usual optimism is gone. With his anxiety growing, Steve doubts his own decision making ability. His confidence slipping, he stopped opening his financial statements and could barely speak to his financial advisor. He thought if his advisor said “hang in there” one more time, he just might blow up.</p>
    <p>Yet Steve felt too embarrassed to talk about his deep worries, even with his wife. It seemed like all he could do was pour another glass of wine and suffer in isolation. If you're like Steve, you're afraid and alone with plenty of company. In a September 2009 Northfield Wellbeing Council poll, 80 percent reported the economy is causing significant stress, up from 66 percent from the previous April. The Restful Nights Institute said 27 percent of people surveyed had sleeplessness because of economic anxiety.</p>
    <p>This process guides you to step back and understand the source of your financial worry—your unique story about the meaning of money. Your money story drives your emotions and decision making—for better and worse. You'll learn a decision making tool for more conscious, effective and satisfying financial and life decisions.</p>
    <p>You'll also examine your core values and strengths—what really matters most to you and how you work at your best. When you use your money and your core strengths to pursue your highest aspirations, life and wealth become balanced. As you commit more fully to your mission and passions, satisfaction grows and money worries melt away.</p>
  </section>

  <p class="program-label">A five session program to:</p>
  <ul class="benefits">
    <li class="teal">Learn a decision making tool to make choices that truly serve your needs</li>
    <li class="purple">Clarify and more fully engage with your purpose and passions</li>
    <li class="rust">Improve your relationship with your financial advisor</li>
    <li class="olive">Feel more in control and confident in your financial life</li>
  </ul>

  <ul class="offer">
    <li>$995 Money back guarantee</li>
    <li>For more information, call Dr. Dana Whitfield, 555-014-0199, dana@harborcirclenetwork.com</li>
  </ul>

  <p class="coach-name">Dana Whitfield, Ph.D</p>
  <p class="coach-bio">is a wealth psychologist<br>with 30 years of experience<br>treating anxiety and stress. She is co-founder<br>and facilitator of Harbor Circle, a peer learning group for<br>high net worth entrepreneurs.</p>
</main>
</body>
</html>
```